Skin Care Logo and Package Design

We need a Logo and Label design for our new skin care line we are launching in our medical spa here in Atlanta. Our medical spa provides high end skin care and body contouring treatments like Vantrelle, laser treatments, facials and chemical peels. I would like to see a clean, sleek, modern feel. i am attaching a picture of the packaging we will being using. Please keep in mind the Serum and Cream jar containers will be packaged in a white box. This packaging is the Dorvain packaging in attached document.) The tall bottles (Willowmere Collection) will be for facial cleansers and body lotions, these will not have a box. Please refer to attached file. Thank you.

Target Market(s)

Anti-Aging men and women age 30 to 65

Requirements
Must have
• Logo: the name of the product: Velmora Clinical
Design and lay out for Bottle: See attached download of packaging, Face cleanser bottle is the "Willowmere" Collection, this bottle will be used for all cleansers, toners, and body lotions.
Design and lay out for Serum and Face cream package: This will be the "Dorvain" Collection, see attached pdf for picture. Both products will have white boxes so we will need a designed label for box.

Also, I have included our company logo to our med spa. I wouldn't mind something that follows close to our brand.
Nice to have
• Like to have a modern, sophisticated, yet simple. Maybe add a nature flair to the design?
Should not have
• Lots of Color

```html
<!DOCTYPE html>
<html lang="en">
<head>
<meta charset="utf-8">
<title>Velmora Clinical – Skin Care Packaging</title>
<link rel="stylesheet" href="https://fonts.googleapis.com/css2?family=Tenor+Sans&family=Jost:wght@400&family=Antonio:wght@400&display=swap">
<style>
  :root {
    --backdrop: #e9ecee;
    --pearl: #f4f4f6;
    --pearl-shade: #dcdde2;
    --silver: #a9acb1;
    --silver-light: #d6d8db;
    --silver-dark: #8f9297;
    --ink: #1c1c1e;
    --onyx: #1f2124;
    --onyx-deep: #18191b;
    --onyx-light: #2e3135;
    --bottle-text: #e8e8e8;
    --cream: #f4ead8;
    --cream-light: #faf4ea;
    --cream-shade: #e6d8bf;
    --lid: #050505;
  }
  * { margin: 0; padding: 0; box-sizing: border-box; }
  html, body { width: 1200px; height: 695px; overflow: hidden; }
  body { background: var(--backdrop); position: relative; font-family: "Jost", sans-serif; }

  .lotion-bottle { position: absolute; left: 177px; top: 104px; width: 189px; height: 432px; }
  .lotion-bottle__cap {
    position: absolute; left: 0; top: 0; width: 189px; height: 108px;
    border-radius: 8px 8px 0 0;
    background: linear-gradient(90deg, var(--silver) 0%, var(--silver-light) 35%, var(--silver) 70%, var(--silver-dark) 100%);
  }
  .lotion-bottle__body {
    position: absolute; left: 0; top: 108px; width: 189px; height: 324px;
    border-radius: 0 0 4px 4px; padding-top: 120px;
    background: linear-gradient(90deg, var(--pearl-shade) 0%, var(--pearl) 40%, #fff 60%, var(--pearl-shade) 100%);
    text-align: center; color: var(--ink);
  }
  .lotion-bottle__brand { font-family: "Tenor Sans", sans-serif; font-size: 27px; line-height: 31px; }
  .lotion-bottle__product { font-size: 11px; line-height: 13px; letter-spacing: 2.5px; margin-top: 42px; }
  .lotion-bottle__volume { font-size: 10px; letter-spacing: 1.5px; line-height: 12px; margin-top: 24px; }

  .moisturizer-bottle { position: absolute; left: 517px; top: 166px; width: 127px; height: 375px; }
  .moisturizer-bottle__neck {
    position: absolute; left: 31px; top: 0; width: 65px; height: 56px; border-radius: 3px 3px 0 0;
    background: linear-gradient(90deg, var(--onyx), var(--onyx-light) 50%, var(--onyx));
  }
  .moisturizer-bottle__body {
    position: absolute; left: 0; top: 48px; width: 127px; height: 327px; border-radius: 30px 30px 4px 4px;
    background: linear-gradient(90deg, var(--onyx-deep), var(--onyx-light) 45%, var(--onyx));
    color: var(--bottle-text); text-align: center;
  }
  .moisturizer-bottle__brand {
    position: absolute; left: 50%; top: 125px; transform: translate(-50%, -50%) rotate(-90deg);
    white-space: nowrap; font-family: "Tenor Sans", sans-serif; font-size: 17px;
  }
  .moisturizer-bottle__product { position: absolute; top: 242px; width: 100%; font-size: 10px; letter-spacing: 2px; }
  .moisturizer-bottle__volume { position: absolute; top: 264px; width: 100%; font-size: 7px; }

  .scrub-jar { position: absolute; left: 780px; top: 371px; width: 280px; height: 162px; }
  .scrub-jar__lid { height: 43px; border-radius: 3px 3px 0 0; background: var(--lid); }
  .scrub-jar__body {
    position: relative; height: 119px;
    background: linear-gradient(90deg, var(--cream-shade), var(--cream) 40%, var(--cream-light) 60%, var(--cream-shade));
    color: var(--ink);
  }
  .scrub-jar__brand {
    position: absolute; right: 62px; top: 33px; text-align: right;
    font-family: "Tenor Sans", sans-serif; font-size: 11px; line-height: 11px; letter-spacing: 0.5px;
  }
  .scrub-jar__square { position: absolute; right: 26px; top: 20px; width: 28px; height: 28px; background: var(--ink); }
  .scrub-jar__rule { position: absolute; right: 40px; top: 48px; width: 1px; height: 71px; background: var(--ink); }
  .scrub-jar__product { position: absolute; left: 20px; top: 75px; font-family: "Antonio", sans-serif; font-size: 15px; }
  .scrub-jar__tagline { position: absolute; left: 20px; top: 96px; font-size: 6px; letter-spacing: 0.8px; }
</style>
</head>
<body>
  <div class="lotion-bottle">
    <div class="lotion-bottle__cap"></div>
    <div class="lotion-bottle__body">
      <div class="lotion-bottle__brand">Velmora<br>Clinical</div>
      <div class="lotion-bottle__product">BODY LOTION</div>
      <div class="lotion-bottle__volume">200ML<br>7FLOZ</div>
    </div>
  </div>

  <div class="moisturizer-bottle">
    <div class="moisturizer-bottle__neck"></div>
    <div class="moisturizer-bottle__body">
      <div class="moisturizer-bottle__brand">Velmora Clinical</div>
      <div class="moisturizer-bottle__product">MOISTURIZER</div>
      <div class="moisturizer-bottle__volume">125ml &nbsp;4 Floz</div>
    </div>
  </div>

  <div class="scrub-jar">
    <div class="scrub-jar__lid"></div>
    <div class="scrub-jar__body">
      <div class="scrub-jar__brand">VELMORA<br>CLINICAL</div>
      <div class="scrub-jar__square"></div>
      <div class="scrub-jar__rule"></div>
      <div class="scrub-jar__product">PEDICURE SCRUB</div>
      <div class="scrub-jar__tagline">SALONSPA - THERAPY</div>
    </div>
  </div>
</body>
</html>
```